Website Design for R M Builders: Showcasing Excellence in General Contracting

R M Builders, a leading general contractor based in California, is seeking a professional and engaging website design to effectively showcase our expertise, services, and commitment to excellence. The website will serve as a digital platform to represent our brand identity, highlight our portfolio, and attract potential clients in various sectors.

Key Objectives:

Reflect Company Identity: The website should accurately reflect the identity and values of R M Builders, including our dedication to quality, professionalism, and client satisfaction.
Showcase Services: Highlight our wide range of general contracting services, including but not limited to construction management, design-build, renovation, and commercial construction.
Portfolio Display: Display an extensive portfolio of past projects completed by R M Builders, showcasing our capabilities, craftsmanship, and successful outcomes.
Client Testimonials: Incorporate client testimonials and case studies to demonstrate our track record of delivering projects on time, within budget, and to the highest standards.
Contact Information: Ensure easy access to contact information, including phone number, email, and physical address, to facilitate communication with potential clients.
Responsive Design: Develop a responsive website design optimized for various devices and screen sizes, ensuring a seamless user experience across desktops, laptops, tablets, and smartphones.
Search Engine Optimization (SEO): Implement SEO best practices to enhance the visibility of the website on search engines, increasing organic traffic and generating leads.
User-Friendly Navigation: Create an intuitive and user-friendly navigation structure that enables visitors to easily find the information they need, such as services, portfolio, testimonials, and contact details.
Visual Appeal: Utilize visually appealing graphics, images, and layout designs to capture the attention of visitors and leave a lasting impression of professionalism and quality.
Compliance and Security: Ensure compliance with industry standards and regulations, as well as implementing necessary security measures to protect user data and privacy.

```html
<!DOCTYPE html>
<html lang="en">
<head>
<meta charset="utf-8">
<title>R M Builders | General Contracting</title>
<link rel="stylesheet" href="https://fonts.googleapis.com/css2?family=Fira+Sans:wght@500;600;700&family=Roboto:wght@400;500;700&display=swap">
<style>
:root{
  --navy:#2c3d6d;
  --navy-deep:#24356a;
  --blue:#15a8e6;
  --blue-dark:#0f93cf;
  --ink:#1b1b1b;
  --text:#333a44;
  --muted:#6b7280;
  --light:#f2f3f5;
  --white:#ffffff;
  --star:#f2c200;
}
*{margin:0;padding:0;box-sizing:border-box}
html,body{width:1200px;height:5055px;overflow:hidden}
body{position:relative;background:var(--white);font-family:"Roboto",Arial,sans-serif;color:var(--text)}
.abs{position:absolute}
h1,h2,h3,h4{font-family:"Fira Sans",Arial,sans-serif}
.section-title{position:absolute;left:0;width:1200px;text-align:center;font-size:30px;font-weight:600;color:var(--ink);letter-spacing:.5px}
.btn{position:absolute;display:flex;align-items:center;justify-content:center;background:var(--blue);color:var(--white);font-family:"Roboto",Arial,sans-serif;font-weight:700;font-size:14px;letter-spacing:.3px;text-transform:uppercase;border-radius:2px}

/* Header / hero */
.hero{position:absolute;left:0;top:0;width:1200px;height:735px;
  background:linear-gradient(180deg,#5f84ad 0%,#8aa7c2 30%,#b8a88a 55%,#c9b394 75%,#b79f7e 100%);
  clip-path:polygon(0 0,100% 0,100% 735px,0 645px)}
.hero-shade{position:absolute;inset:0;background:linear-gradient(90deg,rgba(20,30,50,.55) 0%,rgba(20,30,50,.15) 50%,rgba(0,0,0,0) 100%)}
.hero-machine{position:absolute;left:560px;top:90px;width:640px;height:560px;background:radial-gradient(ellipse at 55% 45%,rgba(214,165,30,.75) 0%,rgba(160,120,40,.35) 45%,rgba(0,0,0,0) 70%)}
.logo{position:absolute;display:flex;align-items:center;gap:8px;font-family:"Fira Sans",Arial,sans-serif;font-weight:700}
.logo-mark{width:16px;height:16px;background:currentColor}
.nav{position:absolute;top:40px;left:0;width:1200px;height:20px}
.nav a{position:absolute;color:var(--white);font-size:15px;text-decoration:none;top:0}
.nav-cta{top:29px;left:955px;width:131px;height:44px;font-size:15px}
.hero-title{position:absolute;left:112px;top:205px;color:var(--white);font-size:50px;line-height:64px;font-weight:600;letter-spacing:1px;text-shadow:0 2px 6px rgba(0,0,0,.35)}
.hero-text{position:absolute;left:112px;top:346px;width:440px;color:var(--white);font-size:15px;line-height:31px}
.hero-dots{position:absolute;left:110px;top:521px;display:flex;gap:8px}
.hero-dots span{width:11px;height:11px;border-radius:50%;background:rgba(255,255,255,.55)}
.hero-dots span.on{background:var(--navy);box-shadow:0 0 0 2px var(--white)}

/* Experience */
.exp-text{position:absolute;left:170px;top:870px;width:860px;text-align:center;font-size:15px;line-height:31px;color:var(--text)}
.feature{position:absolute;top:1003px;width:210px;text-align:center}
.feature-ring{width:110px;height:110px;margin:0 auto;border-radius:50%;display:flex;align-items:center;justify-content:center;border:6px solid var(--navy);box-shadow:0 6px 12px rgba(0,0,0,.15);background:var(--white)}
.feature-ring.alt{border-color:var(--blue)}
.feature-ring svg{width:54px;height:54px}
.feature p{margin-top:22px;font-size:15px;line-height:25px;color:var(--ink)}

/* Services */
.services{position:absolute;left:0;top:1264px;width:1200px;height:672px;
  background:linear-gradient(180deg,#1aa9e6 0%,#19a7e4 100%);
  clip-path:polygon(0 108px,100% 0,100% 100%,0 100%)}
.services-haze{position:absolute;left:300px;top:60px;width:620px;height:250px;background:radial-gradient(ellipse,rgba(30,70,120,.35) 0%,rgba(0,0,0,0) 70%)}
.services .section-title{color:var(--white);top:160px}
.svc-card{position:absolute;top:1503px;width:466px;height:316px;overflow:hidden;box-shadow:0 8px 18px rgba(0,0,0,.25)}
.svc-photo{position:absolute;inset:0}
.svc-body{position:absolute;left:0;top:0;width:100%;height:100%;padding:28px 22px;color:var(--white);background:linear-gradient(90deg,rgba(25,25,25,.95) 0%,rgba(25,25,25,.85) 45%,rgba(25,25,25,0) 70%)}
.svc-body h3{font-size:18px;font-weight:600;letter-spacing:.5px;margin-bottom:14px}
.svc-body li{list-style:none;font-size:14px;line-height:25.6px}
.svc-body li::before{content:"• "}
.svc-body .more{position:absolute;left:22px;bottom:36px;font-size:15px;font-weight:700;text-decoration:underline;color:var(--white)}

/* Projects */
.proj-sub{position:absolute;left:0;top:2092px;width:1200px;text-align:center;font-size:14px;color:var(--text)}
.proj{position:absolute;overflow:hidden}
.proj-photo{position:absolute;inset:0}
.proj-body{position:absolute;left:0;right:0;bottom:0;top:0;padding:0 18px 22px;display:flex;flex-direction:column;justify-content:flex-end;color:var(--white);background:linear-gradient(180deg,rgba(0,0,0,0) 25%,rgba(0,0,0,.55) 60%,rgba(0,0,0,.72) 100%)}
.proj-body h4{font-size:15px;line-height:27px;font-weight:600;margin-bottom:14px}
.proj-body h4.big{font-size:19px;line-height:31px}
.proj-body p{font-size:14px;line-height:30px}
.btn-projects{left:494px;top:2828px;width:212px;height:45px}

/* About */
.about{position:absolute;left:0;top:2930px;width:1200px;height:710px;
  background:linear-gradient(180deg,#2f4070 0%,#2c3d6d 100%);
  clip-path:polygon(0 0,100% 98px,100% 100%,0 100%)}
.about-dots{position:absolute;left:80px;top:3083px;width:100px;height:95px;
  background-image:radial-gradient(circle,rgba(255,255,255,.8) 1.5px,transparent 2px);background-size:14px 14px}
.about-frame{position:absolute;left:124px;top:3128px;width:454px;height:404px;border:2px solid rgba(255,255,255,.85)}
.about-photo{position:absolute;left:112px;top:3112px;width:450px;height:404px;background:linear-gradient(160deg,#dfe6ec 0%,#c9cdd0 30%,#d4a437 55%,#b9773e 80%,#9b5e2f 100%)}
.about-copy{position:absolute;left:635px;top:3130px;width:450px;color:var(--white)}
.about-copy h2{font-size:32px;font-weight:600;letter-spacing:.5px;margin-bottom:18px}
.about-copy .lead{font-size:15px;line-height:31px;font-weight:700;margin-bottom:10px}
.about-copy .body{font-size:15px;line-height:31px}
.btn-about{left:635px;top:3463px;width:131px;height:47px}

/* Testimonials */
.quote{position:absolute;top:3857px;width:308px;height:190px;background:var(--white);border-top:3px solid var(--navy);border-radius:12px;box-shadow:0 6px 16px rgba(0,0,0,.12)}
.quote.mid{border-top-color:var(--blue)}
.quote p{position:absolute;left:24px;right:24px;top:74px;text-align:center;font-size:14px;line-height:26px;color:#555}
.avatar{position:absolute;top:-42px;left:111px;width:86px;height:86px;border-radius:50%;border:4px solid var(--white);background:linear-gradient(180deg,#c8ccd2 0%,#9aa1aa 100%);box-shadow:0 3px 8px rgba(0,0,0,.15)}
.avatar-badge{position:absolute;right:-2px;bottom:2px;width:24px;height:24px;border-radius:50%;background:var(--white);border:2px solid #d9dde2}
.reviewer{position:absolute;top:4078px;width:308px;display:flex;justify-content:center;gap:20px;align-items:center;font-size:14px;font-weight:500;color:var(--ink)}
.stars{color:var(--star);font-size:14px;letter-spacing:1px}
.q-dots{position:absolute;left:582px;top:4140px;display:flex;gap:12px}
.q-dots span{width:9px;height:9px;border-radius:50%;background:#bfe6f8}
.q-dots span.on{background:var(--blue)}

/* Clients */
.clients{position:absolute;left:0;top:4214px;width:1200px;height:408px;background:var(--light)}
.client{position:absolute;top:4377px;width:175px;height:147px;background:var(--white);border:1px solid #dadde2;text-align:center;padding-top:40px}
.client.active{box-shadow:0 6px 18px rgba(0,0,0,.16);border-color:transparent}
.client h4{font-family:"Roboto",Arial,sans-serif;font-size:16px;font-weight:500;color:var(--ink);margin-bottom:10px}
.client.active h4{color:var(--blue)}
.client p{font-size:14px;line-height:30px;color:#444}
.arrow{position:absolute;top:4438px;width:26px;height:26px;border-radius:50%;border:1.5px solid #444;display:flex;align-items:center;justify-content:center}
.arrow.soft{border-color:#aaa}

/* Footer */
.footer{position:absolute;left:0;top:4622px;width:1200px;height:433px;background:var(--navy-deep);color:var(--white)}
.footer h3{position:absolute;top:76px;font-size:20px;font-weight:600}
.links{position:absolute;left:347px;top:106px;list-style:none}
.links li{font-size:14px;line-height:31px;display:flex;align-items:center;gap:10px}
.contact-row{position:absolute;left:541px;display:flex;gap:14px;font-size:14px;line-height:26px}
.contact-ico{width:34px;height:34px;border-radius:50%;background:var(--blue);display:flex;align-items:center;justify-content:center;flex-shrink:0}
.news-text{position:absolute;left:827px;top:106px;width:290px;font-size:14px;line-height:26px}
.news-field{position:absolute;left:832px;top:176px;width:270px;height:32px;border-bottom:1px solid var(--white);font-size:14px}
.btn-sub{left:836px;top:240px;width:133px;height:46px;font-size:17px;text-transform:none;border-radius:6px}
.footer-rule{position:absolute;left:118px;top:366px;width:970px;height:1px;background:rgba(255,255,255,.5)}
.copyright{position:absolute;left:0;top:388px;width:1200px;text-align:center;font-size:14px}
</style>
</head>
<body>

<header class="hero">
  <div class="abs hero-machine" role="img" aria-label="Photo of a yellow excavator on a sandy construction site under a blue sky"></div>
  <div class="hero-shade"></div>
</header>

<div class="logo" style="left:112px;top:50px;color:var(--ink);font-size:22px">
  <span class="logo-mark"></span>R M Builders
</div>

<nav class="nav">
  <a style="left:412px">HOME</a>
  <a style="left:500px">ABOUT US</a>
  <a style="left:621px">SERVICES</a>
  <a style="left:737px">PROJECTS</a>
  <a style="left:857px">CLIENTS</a>
</nav>
<div class="btn nav-cta">CONTACT US</div>

<h1 class="hero-title">WELCOME TO<br>RM BUILDERS</h1>
<p class="hero-text">Since 2013, R M Builders has been a thriving 8(a) certified General Contractor, consistently delivering successful projects to a diverse array of clients.</p>
<div class="btn" style="left:112px;top:457px;width:133px;height:45px">GET STARTED</div>
<div class="hero-dots"><span></span><span class="on"></span><span></span><span></span></div>

<h2 class="section-title" style="top:810px">EXPERIENCE</h2>
<p class="exp-text">With vast experience in the trades, site superintendence, safety, quality control, and all aspects of general contracting, R M Builders can plan, manage and execute building construction projects in all sizes under any delivery method: design-build, CM at Risk, or design-bid-build.</p>

<div class="feature" style="left:73px">
  <div class="feature-ring"><svg viewBox="0 0 48 48" fill="none" stroke="#2c3d6d" stroke-width="2"><rect x="12" y="10" width="24" height="18" rx="2"/><path d="M6 40h8l6-6h10a3 3 0 0 0 0-6h-8"/><path d="M18 16h12M18 22h8" stroke="#15a8e6"/></svg></div>
  <p>Quickly mobilize<br>assets + personnel</p>
</div>
<div class="feature" style="left:283px">
  <div class="feature-ring alt"><svg viewBox="0 0 48 48" fill="none" stroke="#2c3d6d" stroke-width="2"><path d="M24 6l12 5v9c0 8-5 13-12 16-7-3-12-8-12-16v-9z" stroke="#15a8e6"/><path d="M18 21l4 4 8-8"/><path d="M6 42h8l5-5h10a3 3 0 0 0 0-6"/></svg></div>
  <p>Commitment to<br>quality + safety</p>
</div>
<div class="feature" style="left:495px">
  <div class="feature-ring"><svg viewBox="0 0 48 48" fill="none" stroke="#2c3d6d" stroke-width="2"><rect x="12" y="8" width="24" height="32" rx="2"/><path d="M19 8v-2h10v2"/><path d="M18 24l4 4 8-8" stroke="#15a8e6"/><circle cx="35" cy="12" r="5" stroke="#15a8e6"/></svg></div>
  <p>Complete projects<br>on time + on budget</p>
</div>
<div class="feature" style="left:705px">
  <div class="feature-ring alt"><svg viewBox="0 0 48 48" fill="none" stroke="#2c3d6d" stroke-width="2"><circle cx="14" cy="22" r="4"/><circle cx="24" cy="18" r="4" stroke="#15a8e6"/><circle cx="34" cy="22" r="4"/><path d="M8 36v-4a6 6 0 0 1 12 0v4M18 36v-6a6 6 0 0 1 12 0v6M28 36v-4a6 6 0 0 1 12 0v4"/><path d="M24 6v4M16 9l2 3M32 9l-2 3" stroke="#15a8e6"/></svg></div>
  <p>Qualified field +<br>office staff</p>
</div>
<div class="feature" style="left:914px">
  <div class="feature-ring"><svg viewBox="0 0 48 48" fill="none" stroke="#2c3d6d" stroke-width="2"><rect x="10" y="12" width="28" height="22" rx="2"/><circle cx="24" cy="23" r="6" stroke="#15a8e6"/><path d="M24 19v8M22 21h3a1.5 1.5 0 0 1 0 3h-2a1.5 1.5 0 0 0 0 3h3" stroke="#15a8e6" stroke-width="1.4"/><path d="M6 40h36M16 34v6M32 34v6"/></svg></div>
  <p>Value engineering</p>
</div>

<section class="services">
  <div class="services-haze" role="img" aria-label="Faint photo of an excavator at a construction site"></div>
  <h2 class="section-title">OUR SERVICES</h2>
</section>

<article class="svc-card" style="left:112px">
  <div class="svc-photo" role="img" aria-label="Photo of a worker spreading fresh concrete" style="background:linear-gradient(120deg,#3a3a3a 0%,#6a6a66 45%,#a9a49a 65%,#8a7a64 85%,#5c4a36 100%)"></div>
  <div class="svc-body">
    <h3>SPECIALIZED SERVICES</h3>
    <ul><li>Site work</li><li>Concrete</li><li>Landscaping</li><li>Demolition</li><li>Trenching</li><li>Tenant Improvements</li><li>Remodels</li></ul>
    <span class="more">VIEW MORE</span>
  </div>
</article>
<article class="svc-card" style="left:621px">
  <div class="svc-photo" role="img" aria-label="Photo of a carpenter measuring timber in a workshop" style="background:linear-gradient(120deg,#2a2520 0%,#4a3a2a 45%,#9a6a2e 65%,#c8902e 80%,#6b4a28 100%)"></div>
  <div class="svc-body">
    <h3>GENERAL CONTRACTING</h3>
    <ul><li>Quality Control</li><li>Service &amp;<br>&nbsp;&nbsp;Maintenance</li><li>Risk Analysis</li><li>Estimating</li><li>Design-Build</li><li>Project Management</li></ul>
    <span class="more">VIEW MORE</span>
  </div>
</article>

<h2 class="section-title" style="top:2032px">OUR PROJECTS</h2>
<p class="proj-sub">*in progress or completed within the last five (5) years</p>

<article class="proj" style="left:112px;top:2148px;width:470px;height:306px">
  <div class="proj-photo" role="img" aria-label="Photo of engineers in hard hats reviewing a roof project" style="background:linear-gradient(160deg,#d9e2ea 0%,#a6b2bd 40%,#6e6a66 75%,#4a4240 100%)"></div>
  <div class="proj-body"><h4 class="big">Job Order Contract (JOC) | 2016-2023 | County of Mesa Verde</h4><p>Mesa Verde, CA | Task Orders Awarded: 155 Total<br>Awarded Value: $20,000,000+</p></div>
</article>
<article class="proj" style="left:600px;top:2148px;width:235px;height:306px">
  <div class="proj-photo" role="img" aria-label="Photo of a team reviewing contract paperwork at a table" style="background:linear-gradient(160deg,#6a4a3a 0%,#8b6a55 40%,#3e3a3a 100%)"></div>
  <div class="proj-body"><h4>SABER/IDIQ 5-year<br>Contract | Air Command</h4><p>Ridgeway AFB, CA | Task<br>Orders Awarded: 150+ Total</p></div>
</article>
<article class="proj" style="left:853px;top:2148px;width:235px;height:306px">
  <div class="proj-photo" role="img" aria-label="Photo of a building interior under renovation with timber framing" style="background:linear-gradient(160deg,#b8a690 0%,#8e7a64 45%,#4a3e34 100%)"></div>
  <div class="proj-body"><h4>Building Renovation, B.<br>6408 | Sierra Reserve</h4><p>Camp Alder, CA Value:<br>$1,001,747</p></div>
</article>
<article class="proj" style="left:112px;top:2474px;width:235px;height:305px">
  <div class="proj-photo" role="img" aria-label="Photo of a worker in orange coveralls operating equipment" style="background:linear-gradient(160deg,#8a8a88 0%,#d06a2a 45%,#6a4a36 100%)"></div>
  <div class="proj-body"><h4>Renovate Air Traffic<br>Control Tower | FWC,</h4><p>Ridgeway AFB, CA | Value:<br>$1,166,452</p></div>
</article>
<article class="proj" style="left:365px;top:2474px;width:235px;height:305px">
  <div class="proj-photo" role="img" aria-label="Photo of technicians servicing red fire suppression piping" style="background:linear-gradient(160deg,#c23a3a 0%,#8a2a2a 40%,#3a4a6a 75%,#2a2a2a 100%)"></div>
  <div class="proj-body"><h4>Repair Fire Suppression<br>Sys. B. 8472 &amp; 8473 |</h4><p>Ridgeway AFB, CA | Value:<br>$1,766,711</p></div>
</article>
<article class="proj" style="left:617px;top:2474px;width:471px;height:305px">
  <div class="proj-photo" role="img" aria-label="Photo of a worker on scaffolding inside an office renovation" style="background:linear-gradient(160deg,#e2e4e6 0%,#b9b4ac 40%,#8c6a44 70%,#4a3a2e 100%)"></div>
  <div class="proj-body"><h4 class="big">Renovations of Offices, B. 510 | FWC,<br>Southland Dist.</h4><p>Naval Base Harbor Point, CA | Value:<br>$697,925</p></div>
</article>

<div class="btn btn-projects">VIEW MORE PROJECTS</div>

<section class="about"></section>
<div class="about-dots"></div>
<div class="about-frame"></div>
<div class="about-photo" role="img" aria-label="Photo of a yellow excavator digging a sand pile"></div>
<div class="about-copy">
  <h2>ABOUT US</h2>
  <p class="lead">Since 2013, R M Builders has been a thriving 8(a) certified General Contractor, consistently delivering successful projects to a diverse array of clients.</p>
  <p class="body">With vast experience in the trades, site superintendence, safety, quality control, and all aspects of general contracting, R M Builders can plan, manage and execute building construction projects in all sizes under any delivery method: design-build, CM at Risk, or design-bid-build.</p>
</div>
<div class="btn btn-about">VIEW MORE</div>

<h2 class="section-title" style="top:3725px">WHAT OUR CLIENTS SAYS</h2>

<div class="quote" style="left:112px">
  <div class="avatar" role="img" aria-label="Client portrait"><span class="avatar-badge"></span></div>
  <p>Sed ut perspiciatis unde omnis iste natus error sit voluptatem accusantium doloremque laudantium, totam rem aperiam, eaque ipsa</p>
</div>
<div class="quote mid" style="left:445px">
  <div class="avatar" role="img" aria-label="Client portrait"><span class="avatar-badge"></span></div>
  <p>Sed ut perspiciatis unde omnis iste natus error sit voluptatem accusantium doloremque laudantium, totam rem aperiam, eaque ipsa</p>
</div>
<div class="quote" style="left:778px">
  <div class="avatar" role="img" aria-label="Client portrait"><span class="avatar-badge"></span></div>
  <p>Sed ut perspiciatis unde omnis iste natus error sit voluptatem accusantium doloremque laudantium, totam rem aperiam, eaque ipsa</p>
</div>
<div class="reviewer" style="left:112px">Jhon Deo <span class="stars">★★★★★</span></div>
<div class="reviewer" style="left:445px">Jhon Deo <span class="stars">★★★★★</span></div>
<div class="reviewer" style="left:778px">Jhon Deo <span class="stars">★★★★★</span></div>
<div class="q-dots"><span></span><span class="on"></span><span></span></div>

<section class="clients"></section>
<h2 class="section-title" style="top:4303px">CLIENTS</h2>
<div class="arrow soft" style="left:42px"><svg width="10" height="10" viewBox="0 0 10 10"><path d="M6.5 1.5L3 5l3.5 3.5" fill="none" stroke="#888" stroke-width="1.4"/></svg></div>
<div class="arrow" style="left:1122px"><svg width="10" height="10" viewBox="0 0 10 10"><path d="M3.5 1.5L7 5 3.5 8.5" fill="none" stroke="#333" stroke-width="1.4"/></svg></div>
<div class="client" style="left:112px;padding-top:48px"><h4>Air Command</h4><p>Ridgeway AFB, CA</p></div>
<div class="client" style="left:312px"><h4>Air Command</h4><p>31CES Kestrel<br>SFB, CA</p></div>
<div class="client active" style="left:512px"><h4>Air Command</h4><p>31CONS Kestrel<br>SFB, CA</p></div>
<div class="client" style="left:713px;padding-top:48px"><h4>Ridgeline Corps</h4><p>Ft. Granite, CA</p></div>
<div class="client" style="left:913px"><h4>Aero Research</h4><p>Skyline Flight<br>Research Ctr</p></div>

<footer class="footer">
  <div class="logo" style="left:118px;top:130px;color:var(--white);font-size:24px"><span class="logo-mark"></span>R M Builders</div>

  <h3 style="left:347px">Quick Links</h3>
  <ul class="links">
    <li><svg width="12" height="12" viewBox="0 0 12 12"><path d="M1 6h9M6 2l4 4-4 4" fill="none" stroke="#fff" stroke-width="2"/></svg>Home</li>
    <li><svg width="12" height="12" viewBox="0 0 12 12"><path d="M1 6h9M6 2l4 4-4 4" fill="none" stroke="#fff" stroke-width="2"/></svg>About Us</li>
    <li><svg width="12" height="12" viewBox="0 0 12 12"><path d="M1 6h9M6 2l4 4-4 4" fill="none" stroke="#fff" stroke-width="2"/></svg>Services</li>
    <li><svg width="12" height="12" viewBox="0 0 12 12"><path d="M1 6h9M6 2l4 4-4 4" fill="none" stroke="#fff" stroke-width="2"/></svg>Projects</li>
    <li><svg width="12" height="12" viewBox="0 0 12 12"><path d="M1 6h9M6 2l4 4-4 4" fill="none" stroke="#fff" stroke-width="2"/></svg>Clients</li>
    <li><svg width="12" height="12" viewBox="0 0 12 12"><path d="M1 6h9M6 2l4 4-4 4" fill="none" stroke="#fff" stroke-width="2"/></svg>Contact Us</li>
  </ul>

  <h3 style="left:541px">Contact Us</h3>
  <div class="contact-row" style="top:106px">
    <span class="contact-ico"><svg width="16" height="16" viewBox="0 0 16 16"><path d="M8 1a5 5 0 0 0-5 5c0 4 5 9 5 9s5-5 5-9a5 5 0 0 0-5-5z" fill="#fff"/><circle cx="8" cy="6" r="2" fill="#15a8e6"/></svg></span>
    <span>P.O. Box 2480<br>Arroyo, CA 93400<br>www.rmbuilders.biz</span>
  </div>
  <div class="contact-row" style="top:200px;align-items:center">
    <span class="contact-ico"><svg width="16" height="16" viewBox="0 0 16 16"><rect x="2" y="4" width="12" height="9" rx="1" fill="#fff"/><path d="M2.5 4.5L8 9l5.5-4.5" fill="none" stroke="#15a8e6" stroke-width="1.3"/></svg></span>
    <span>info@rmbuilders.biz</span>
  </div>
  <div class="contact-row" style="top:259px;align-items:center">
    <span class="contact-ico"><svg width="16" height="16" viewBox="0 0 16 16"><path d="M4 2l2.5 3-1.5 1.5a8 8 0 0 0 4.5 4.5L11 9.5l3 2.5-1.5 2C7 14 2 9 2 3.5z" fill="#fff"/></svg></span>
    <span>(805) 555-0142</span>
  </div>

  <h3 style="left:827px">Sign Up Our Newsletter</h3>
  <p class="news-text">Lorem ipsum dolor sit amet,consectetur adipiscing elit,adipiscing elit.</p>
  <div class="news-field">Email</div>
  <div class="btn btn-sub">Subscribe</div>

  <div class="footer-rule"></div>
  <p class="copyright">Copyrights @2024.R M Builders.All Rights Reserved</p>
</footer>

</body>
</html>
```